Business Card Design

New business, starting out small. High end residential/ commercial building company in Sydney Australia's prestigious Eastern suburbs, perfection is our motto and we want our marketing design to reflect that.

Therefore marketing towards high end clients. Looking for design concepts that will portray this image and will appeal to both male and females, prototype has been included- see images. Although we are open to ideas we have included this to give direction.

DARK Navy and white is the colour scheme, as per image provided. Logo ideas welcomed, however design is preferred simple, modern and sophisticated.

This business card will be the template and inspiration for website, t-shirt, banners etc to come so if you want the business, show us your design!

Industry/Entity Type

Marketing

Contact Information for Business Card

Company name: Tallow Ridge Building
Catch phrase: Your vision
Owner/operator: Garreth Pell
Phone: 0468172905
Website: www.tallowridgebuilding.com.au
Licence No 518294K
ABN 72 913 804
Email address
(displayed on back of card):info@tallowridgebuilding.com.au

```html
<!DOCTYPE html>
<html lang="en">
<head>
<meta charset="utf-8">
<title>Tallow Ridge Building — Business Card</title>
<link href="https://fonts.googleapis.com/css2?family=Cinzel:wght@500;600&family=Didact+Gothic&display=swap" rel="stylesheet">
<style>
  :root {
    --backdrop: #b4b4b4;
    --navy: #0e1a2b;
    --navy-line: #13233d;
    --white: #ffffff;
    --silver-light: #f2f2f2;
    --silver-mid: #a9abae;
    --silver-dark: #6e7174;
    --muted: #9a9ea3;
    --faint: #e4e4e4;
    --sans: "Didact Gothic", "Century Gothic", sans-serif;
    --serif: "Cinzel", "Trajan Pro", serif;
  }
  * { box-sizing: border-box; margin: 0; padding: 0; }
  html, body { width: 1200px; height: 900px; overflow: hidden; }
  body {
    background: var(--backdrop);
    position: relative;
    font-family: var(--sans);
  }
  .card {
    position: absolute;
    top: 300px;
    width: 530px;
    height: 303px;
    box-shadow: 0 14px 28px rgba(0,0,0,.28);
  }
  /* Front */
  .card-front { left: 45px; background: var(--navy); }
  .front-frame {
    position: absolute;
    inset: 13px;
    border: 4px solid transparent;
    border-image: linear-gradient(135deg, var(--silver-dark), var(--silver-light) 35%, var(--silver-mid) 60%, var(--silver-light) 85%, var(--silver-dark)) 1;
  }
  .owner {
    position: absolute;
    top: 24px;
    right: 30px;
    text-align: right;
  }
  .owner-name { color: var(--white); font-size: 18px; letter-spacing: .3px; }
  .owner-role { color: var(--muted); font-size: 15px; margin-top: 2px; }
  .brand {
    position: absolute;
    top: 48px;
    left: 0;
    width: 100%;
    text-align: center;
  }
  .brand-mark {
    display: block;
    margin: 0 auto 12px;
    width: 70px;
    height: 70px;
  }
  .brand-name {
    color: var(--white);
    font-family: var(--serif);
    font-weight: 600;
    font-size: 18px;
    letter-spacing: 1.2px;
  }
  .brand-tagline {
    color: var(--white);
    font-family: var(--serif);
    font-weight: 500;
    font-size: 16px;
    letter-spacing: 6px;
    margin-top: 0;
  }
  .contact {
    position: absolute;
    left: 26px;
    bottom: 30px;
    color: var(--white);
    font-size: 15px;
    line-height: 1.25;
  }
  .contact-line { display: flex; align-items: center; gap: 3px; }
  .contact-icon { width: 13px; height: 13px; }
  .licence { color: var(--muted); font-size: 9px; padding-left: 18px; letter-spacing: .2px; }
  /* Back */
  .card-back { left: 625px; background: var(--white); }
  .back-frame {
    position: absolute;
    inset: 15px;
    border: 4px solid var(--navy-line);
  }
  .back-decoration {
    position: absolute;
    left: 50%;
    top: 50%;
    width: 150px;
    height: 150px;
    transform: translate(-50%, -50%);
    background: var(--faint);
  }
  .back-email {
    position: absolute;
    top: 50%;
    left: 0;
    width: 100%;
    text-align: center;
    transform: translateY(-60%);
    color: var(--navy);
    font-size: 21px;
    letter-spacing: .2px;
  }
</style>
</head>
<body>
  <section class="card card-front" aria-label="Business card front">
    <div class="front-frame"></div>
    <div class="owner">
      <p class="owner-name">Garreth Pell</p>
      <p class="owner-role">Owner/operator</p>
    </div>
    <div class="brand">
      <svg class="brand-mark" viewBox="0 0 70 70" aria-hidden="true">
        <defs>
          <linearGradient id="silver" x1="0" y1="0" x2="1" y2="1">
            <stop offset="0" stop-color="#f4f4f4"/>
            <stop offset=".5" stop-color="#9da0a4"/>
            <stop offset="1" stop-color="#e6e6e6"/>
          </linearGradient>
        </defs>
        <rect x="4" y="4" width="62" height="62" fill="none" stroke="url(#silver)" stroke-width="5"/>
      </svg>
      <p class="brand-name">TALLOW RIDGE BUILDING</p>
      <p class="brand-tagline">Your vision</p>
    </div>
    <div class="contact">
      <p class="contact-line">
        <svg class="contact-icon" viewBox="0 0 16 16" aria-hidden="true"><path d="M3 1.5l3 .5 1 3.5-2 1.3a9 9 0 0 0 4.2 4.2L10.5 9l3.5 1 .5 3-2 1.5C6.5 14 2 9.5 1.5 3.5z" fill="#c9ccd0"/></svg>
        0468172905
      </p>
      <p class="contact-line">
        <svg class="contact-icon" viewBox="0 0 16 16" aria-hidden="true"><g fill="none" stroke="#c9ccd0" stroke-width="1.2"><circle cx="8" cy="8" r="6.5"/><ellipse cx="8" cy="8" rx="2.8" ry="6.5"/><path d="M1.5 8h13M2.6 4.5h10.8M2.6 11.5h10.8"/></g></svg>
        www.tallowridgebuilding.com.au
      </p>
      <p class="licence">Licence No 518294K ABN 72 913 804</p>
    </div>
  </section>

  <section class="card card-back" aria-label="Business card back">
    <div class="back-frame"></div>
    <div class="back-decoration" aria-hidden="true"></div>
    <p class="back-email">info@tallowridgebuilding.com.au</p>
  </section>
</body>
</html>
```